Life Coach for Lawyers Business Card Design

Elegant, original, business card design for life coaching service for associate attorneys who work in big law and struggle with stress, overwhelm, and time management. Double sided design.

Target Market(s)

Women associate attorneys who work in big law and struggle with stress, overwhelm, and time management.

Industry/Entity Type

Life Coaching

Contact Information for Business Card

Marissa Pendrell
Life Coach
518.677.3941
calmbriefcounsel.net
marissa@calmbriefcounsel.net
@calmbriefcounsel (Instagram)

Font styles to use
Other font styles liked:
• Silver South font duo. See uploaded files.

Requirements
Must have
• Icons for phone, website, email, and Instagram instead of words. Specific colors used in my logo (171B2B, 421121, FFFFFF)
Nice to have
• Foil. Embossed. Feminine design.
Should not have
• Any colors other than those used in logo. See uploaded files.

```html
<!DOCTYPE html>
<html lang="en">
<head>
<meta charset="utf-8">
<title>Marissa Pendrell – Business Card</title>
<link rel="stylesheet" href="https://fonts.googleapis.com/css2?family=Raleway:wght@400;500&family=Lato:wght@400&display=swap">
<style>
  :root {
    --navy: #171B2B;
    --navy-deep: #0E1226;
    --slate: #5A6178;
    --plum: #421121;
    --white: #FFFFFF;
    --tan-1: #C4925F;
    --tan-2: #9B7048;
    --tan-3: #5E4530;
    --mist: #E8ECEC;
  }
  * { margin: 0; padding: 0; box-sizing: border-box; }
  html, body { width: 947px; height: 1200px; overflow: hidden; background: var(--white); }
  .canvas { position: relative; width: 947px; height: 1200px; background: var(--white); border-top: 1px solid var(--navy); }

  .card-front { position: absolute; left: 0; top: 0; width: 947px; height: 569px; }
  .divider-band { position: absolute; left: 0; top: 569px; width: 947px; height: 62px; background: var(--navy-deep); }
  .card-back { position: absolute; left: 0; top: 631px; width: 947px; height: 569px; }

  .identity { position: absolute; left: 62px; top: 98px; }
  .identity-name { font-family: 'Raleway', sans-serif; font-weight: 400; font-size: 38px; line-height: 1; color: var(--navy); letter-spacing: 0.2px; }
  .identity-name .first { color: var(--plum); }
  .identity-role { font-family: 'Lato', sans-serif; font-size: 22px; color: var(--navy); margin-top: 8px; }

  .contact-icons { position: absolute; left: 62px; top: 252px; width: 64px; }
  .contact-icon { width: 64px; height: 64px; display: flex; align-items: center; justify-content: center; }
  .contact-icon.phone { background: var(--tan-1); }
  .contact-icon.web { background: var(--tan-2); }
  .contact-icon.social { background: var(--tan-3); }

  .contact-text { position: absolute; left: 143px; font-family: 'Lato', sans-serif; font-size: 21.5px; color: var(--navy); line-height: 28px; }
  .contact-text.phone { top: 269px; }
  .contact-text.web { top: 321px; }
  .contact-text.social { top: 396px; }

  .portrait-splash { position: absolute; left: 404px; top: 6px; width: 543px; height: 560px; }
  .sunset-splash { position: absolute; left: 14px; top: 16px; width: 545px; height: 550px; }

  .brand-seal { position: absolute; left: 627px; top: 152px; width: 216px; height: 216px; border: 2px solid var(--plum); border-radius: 50%; display: flex; align-items: center; justify-content: center; text-align: center; }
  .brand-name { font-family: 'Raleway', sans-serif; font-weight: 500; font-size: 24px; line-height: 1.25; color: var(--plum); letter-spacing: 1px; }
</style>
</head>
<body>
<main class="canvas">

  <section class="card-front">
    <svg class="portrait-splash" viewBox="0 0 543 560" role="img" aria-label="Portrait of the coach in a navy blazer, framed by a navy brush-stroke splash">
      <defs>
        <linearGradient id="portraitTone" x1="0" y1="0" x2="1" y2="1">
          <stop offset="0" stop-color="#0E1226"/>
          <stop offset="0.55" stop-color="#171B2B"/>
          <stop offset="0.8" stop-color="#2A3352"/>
          <stop offset="1" stop-color="#C9A48C"/>
        </linearGradient>
      </defs>
      <path fill="var(--slate)" opacity="0.85" d="M150 70 L230 40 L300 60 L380 20 L430 50 L480 40 L520 110 L500 200 L530 260 L510 360 L470 430 L420 480 L350 470 L290 520 L230 500 L170 530 L120 480 L70 420 L80 360 L40 300 L70 220 L60 150 Z"/>
      <path fill="url(#portraitTone)" d="M140 110 L210 80 L270 100 L330 70 L400 90 L460 80 L500 150 L490 230 L510 300 L480 380 L430 440 L360 450 L300 490 L240 470 L180 490 L140 440 L100 390 L110 330 L70 280 L100 210 L90 160 Z"/>
      <g stroke="var(--navy)" stroke-width="2" opacity="0.6">
        <line x1="40" y1="120" x2="90" y2="140"/><line x1="30" y1="230" x2="80" y2="240"/>
        <line x1="50" y1="380" x2="100" y2="370"/><line x1="110" y1="500" x2="150" y2="470"/>
        <line x1="490" y1="30" x2="520" y2="70"/><line x1="520" y1="420" x2="500" y2="450"/>
      </g>
    </svg>

    <header class="identity">
      <h1 class="identity-name"><span class="first">MARISSA</span> Pendrell</h1>
      <p class="identity-role">Life Coach</p>
    </header>

    <div class="contact-icons">
      <div class="contact-icon phone">
        <svg width="30" height="30" viewBox="0 0 24 24" aria-hidden="true"><path fill="var(--white)" d="M6.6 10.8c1.4 2.8 3.8 5.1 6.6 6.6l2.2-2.2c.3-.3.7-.4 1-.2 1.1.4 2.3.6 3.6.6.6 0 1 .4 1 1V20c0 .6-.4 1-1 1C10.6 21 3 13.4 3 4c0-.6.4-1 1-1h3.5c.6 0 1 .4 1 1 0 1.3.2 2.5.6 3.6.1.3 0 .7-.2 1z"/></svg>
      </div>
      <div class="contact-icon web">
        <svg width="32" height="30" viewBox="0 0 32 30" aria-hidden="true"><rect x="3" y="4" width="26" height="17" fill="none" stroke="var(--white)" stroke-width="2.5"/><rect x="13" y="21" width="6" height="4" fill="var(--white)"/><rect x="9" y="25" width="14" height="2" fill="var(--white)"/></svg>
      </div>
      <div class="contact-icon social">
        <svg width="30" height="30" viewBox="0 0 30 30" aria-hidden="true"><circle cx="15" cy="15" r="11" fill="none" stroke="var(--white)" stroke-width="2.5"/></svg>
      </div>
    </div>

    <p class="contact-text phone">+1 518.677.3941</p>
    <p class="contact-text web">calmbriefcounsel.net<br>marissa@calmbriefcounsel.net</p>
    <p class="contact-text social">@calmbriefcounsel</p>
  </section>

  <div class="divider-band"></div>

  <section class="card-back">
    <svg class="sunset-splash" viewBox="0 0 545 550" role="img" aria-label="Silhouette of a woman leaping against a golden sunset sky, framed by a soft brush-stroke splash">
      <defs>
        <radialGradient id="sunsetTone" cx="0.4" cy="0.55" r="0.6">
          <stop offset="0" stop-color="#FBF6EC"/>
          <stop offset="0.45" stop-color="#F2D9A8"/>
          <stop offset="0.8" stop-color="#E3B57C"/>
          <stop offset="1" stop-color="#D8A99C"/>
        </radialGradient>
      </defs>
      <path fill="var(--mist)" d="M90 70 L180 40 L260 60 L330 30 L420 70 L500 110 L520 200 L500 290 L530 360 L490 450 L420 480 L350 530 L270 510 L190 540 L120 490 L60 440 L40 360 L20 280 L50 200 L30 130 Z"/>
      <path fill="url(#sunsetTone)" d="M120 100 L200 80 L270 95 L340 75 L430 110 L480 180 L470 260 L495 330 L455 420 L390 450 L330 490 L260 470 L190 495 L130 450 L90 390 L80 320 L60 250 L90 180 L80 130 Z"/>
    </svg>

    <div class="brand-seal">
      <p class="brand-name">CALM BRIEF<br>COUNSEL</p>
    </div>
  </section>

</main>
</body>
</html>
```